Kivora - a fintech company - business card

We need a business card design for our Payments Technology company in Sydney, Australia. We provide business with payment solutions expanding across EFTPOS machines, online payment gateways and mobile payment solutions. We would like to see designs that are clean, classy and professional.
Target Market(s)
Business professionals, executives, c-suite
Industry/Entity Type
Fintech
Contact Information for Business Card
Will be on 400gsm. Logo will most likely be spot gloss unless designer recommends otherwise.
Font styles to use
Sans Serif
Requirements
Must have
- We need our website (kivora.com.au), email (contact@kivora.com.au), mobile (0455 806 274) and direct phone number (02 7391 5082) to feature on the card along with our logo (attached) and the words "EFTPOS | ONLINE | MOBILE"
- Font = Roboto

```html
<!DOCTYPE html>
<html lang="en">
<head>
<meta charset="UTF-8">
<title>Kivora – Business Card</title>
<link rel="stylesheet" href="https://fonts.googleapis.com/css2?family=Roboto:wght@300;400;700;900&display=swap">
<style>
  :root {
    --backdrop: #2e3034;
    --card-white: #ffffff;
    --brand-blue: #1f67a0;
    --brand-blue-dark: #175689;
    --ink-grey: #555a60;
    --logo-grey: #5f6368;
    --silver: #cfd3d8;
    --tagline: #a9c6de;
  }
  * { box-sizing: border-box; margin: 0; padding: 0; }
  html, body {
    width: 1200px; height: 900px; overflow: hidden;
    background: var(--backdrop);
    font-family: 'Roboto', Arial, sans-serif;
  }
  .canvas {
    position: relative; width: 1200px; height: 900px;
    display: flex; align-items: center; justify-content: center; gap: 64px;
  }
  .card {
    border-radius: 26px;
    box-shadow: 0 18px 40px rgba(0,0,0,.45);
    position: relative; overflow: hidden;
  }
  /* Front – portrait */
  .card-front {
    width: 340px; height: 556px;
    background: var(--card-white);
  }
  .brand-lockup {
    position: absolute; left: 0; right: 0; top: 120px;
    display: flex; align-items: center; justify-content: center; gap: 14px;
  }
  .brand-dot {
    width: 58px; height: 58px; border-radius: 50%;
    background: var(--brand-blue);
  }
  .brand-name {
    font-weight: 900; font-size: 34px; letter-spacing: 0.5px;
    color: var(--logo-grey); text-transform: uppercase;
  }
  .person {
    position: absolute; left: 96px; top: 272px;
  }
  .person-name {
    font-weight: 300; font-size: 24px; color: var(--ink-grey);
    letter-spacing: 0.5px;
  }
  .person-title {
    font-weight: 400; font-size: 15px; color: var(--brand-blue);
    margin-top: 2px;
  }
  .contact-list {
    list-style: none; margin-top: 22px;
  }
  .contact-list li {
    display: flex; align-items: center; gap: 10px;
    font-size: 15px; color: var(--ink-grey); line-height: 1;
    margin-bottom: 11px;
  }
  .contact-list svg { width: 13px; height: 13px; flex: none; fill: var(--brand-blue); }

  /* Back – landscape */
  .card-back {
    width: 556px; height: 340px;
    background: linear-gradient(135deg, var(--brand-blue) 0%, var(--brand-blue-dark) 100%);
  }
  .back-lockup {
    position: absolute; left: 0; right: 0; top: 112px;
    display: flex; align-items: center; justify-content: center; gap: 18px;
  }
  .back-lockup .brand-dot { width: 80px; height: 80px; background: var(--silver); }
  .back-lockup .brand-name { font-size: 48px; color: var(--silver); }
  .tagline {
    position: absolute; left: 0; right: 0; top: 222px;
    text-align: center; font-size: 12px; font-weight: 400;
    letter-spacing: 4px; color: var(--tagline);
  }
</style>
</head>
<body>
<main class="canvas">
  <section class="card card-front" aria-label="Business card front">
    <div class="brand-lockup">
      <span class="brand-dot"></span>
      <span class="brand-name">Kivora</span>
    </div>
    <div class="person">
      <p class="person-name">YOUR NAME</p>
      <p class="person-title">Job Title</p>
      <ul class="contact-list">
        <li>
          <svg viewBox="0 0 16 16" aria-hidden="true"><path d="M4 0h8a1 1 0 0 1 1 1v14a1 1 0 0 1-1 1H4a1 1 0 0 1-1-1V1a1 1 0 0 1 1-1zm1 2v10h6V2zm3 11a1 1 0 1 0 0 2 1 1 0 0 0 0-2z"/></svg>
          0455 806 274
        </li>
        <li>
          <svg viewBox="0 0 16 16" aria-hidden="true"><path d="M3.6 1.2 5.8 3.4c.4.4.4 1 0 1.4L4.6 6a9 9 0 0 0 5.4 5.4l1.2-1.2c.4-.4 1-.4 1.4 0l2.2 2.2c.4.4.4 1 0 1.4l-1.3 1.3C12 16 5 13 1.9 7 .4 4.2.6 2.7 2.2 1.2c.4-.4 1-.4 1.4 0z"/></svg>
          02 7391 5082
        </li>
        <li>
          <svg viewBox="0 0 16 16" aria-hidden="true"><path d="M0 3h16v10H0zm1.5 1.5v.3L8 9l6.5-4.2v-.3zm0 2.1v4.9h13V6.6L8 10.8z"/></svg>
          contact@kivora.com.au
        </li>
        <li>
          <svg viewBox="0 0 16 16" aria-hidden="true"><path d="M8 0a8 8 0 1 0 0 16A8 8 0 0 0 8 0zm5.9 7h-2.5a12 12 0 0 0-1-4.6A6 6 0 0 1 13.9 7zM8 2c.7.9 1.3 2.7 1.4 5H6.6C6.7 4.7 7.3 2.9 8 2zM5.6 2.4A12 12 0 0 0 4.6 7H2.1a6 6 0 0 1 3.5-4.6zM2.1 9h2.5a12 12 0 0 0 1 4.6A6 6 0 0 1 2.1 9zM8 14c-.7-.9-1.3-2.7-1.4-5h2.8c-.1 2.3-.7 4.1-1.4 5zm2.4-.4a12 12 0 0 0 1-4.6h2.5a6 6 0 0 1-3.5 4.6z"/></svg>
          kivora.com.au
        </li>
      </ul>
    </div>
  </section>

  <section class="card card-back" aria-label="Business card back">
    <div class="back-lockup">
      <span class="brand-dot"></span>
      <span class="brand-name">Kivora</span>
    </div>
    <p class="tagline">EFTPOS | ONLINE | MOBILE</p>
  </section>
</main>
</body>
</html>
```